Business card for a boutique travel agency VELARIEN

we need a business card design - double sided. We would like to have a very elegant, sophisticated but modern design. we are travel consultants and our business focus is Europe, mainly the city of Paris. We would like to receive designs in white and silver, black color but if you are confident that we should pick up a color to make it different and more beautful...go ahead! We are going to give business cards to our clients and business partners. It is important to be perceived as elegant, modern and trustful. Please check jpg references.

Target Market(s)

Velarien primary clients are individuals, couples and affinity groups of high-net-worth who travel for leisure at least once per year. Seeking the ultimate travel experience, the target clients demand the finest quality activities and accommodations accompanied by a superior level of service.

Industry/Entity Type

Travel Industry

Contact Information for Business Card

Lucinda Farrow
- lucinda@velarien-example.com
- +55 11 98347.2516
- velarien-example.com
- unique travel experiences (we would like to see this signature printed as a detail)

Font styles to use
Sans Serif

Colors

Designer to choose colors to be used in the design.

Requirements
Must have
• the Velarien logo that I have attached
Nice to have
• we would like to have some nice detail, something different that shows that we care about,... we are detail oriented.
Should not have
• decorative fonts

```html
<!DOCTYPE html>
<html lang="en">
<head>
<meta charset="utf-8">
<title>Velarien — Business Card</title>
<link rel="stylesheet" href="https://fonts.googleapis.com/css2?family=Jost:wght@300;400&display=swap">
<style>
  :root {
    --backdrop: #2e2926;
    --card: #111111;
    --card-edge: #1c1c1c;
    --ink: #f2f2f2;
    --ink-soft: #d9d9d9;
    --silver: #bfc2c6;
  }
  * { margin: 0; padding: 0; box-sizing: border-box; }
  html, body { width: 1200px; height: 780px; overflow: hidden; }
  body {
    background: var(--backdrop);
    font-family: "Jost", sans-serif;
    color: var(--ink);
    position: relative;
  }
  .card {
    position: absolute;
    top: 240px;
    width: 510px;
    height: 300px;
    border-radius: 20px;
    background: var(--card);
    box-shadow: 0 18px 40px rgba(0,0,0,0.45);
    border: 1px solid var(--card-edge);
  }
  .card--front { left: 75px; }
  .card--back  { left: 615px; }

  .holder-name {
    position: absolute;
    left: 40px;
    top: 118px;
    font-size: 15px;
    font-weight: 400;
    letter-spacing: 0.04em;
    text-transform: uppercase;
  }
  .brand {
    position: absolute;
    left: 240px;
    top: 62px;
  }
  .brand-name {
    font-size: 25px;
    font-weight: 300;
    letter-spacing: 0.42em;
    color: var(--ink);
    line-height: 1;
  }
  .brand-tagline {
    margin-top: 8px;
    font-size: 15px;
    font-weight: 300;
    letter-spacing: 0.06em;
    color: var(--ink-soft);
  }
  .contact-line {
    position: absolute;
    left: 40px;
    bottom: 36px;
    display: flex;
    align-items: center;
    gap: 9px;
    font-size: 13px;
    font-weight: 300;
    letter-spacing: 0.02em;
    color: var(--ink-soft);
    white-space: nowrap;
  }
  .contact-dot {
    width: 5px; height: 5px;
    border-radius: 50%;
    background: var(--ink-soft);
  }
  .back-brand {
    position: absolute;
    inset: 0;
    display: flex;
    align-items: center;
    justify-content: center;
    font-size: 30px;
    font-weight: 300;
    letter-spacing: 0.45em;
    padding-left: 0.45em;
    color: var(--silver);
  }
</style>
</head>
<body>
  <section class="card card--front" aria-label="Business card front">
    <p class="holder-name">Lucinda Farrow</p>
    <div class="brand">
      <p class="brand-name">VELARIEN</p>
      <p class="brand-tagline">unique travel experiences</p>
    </div>
    <p class="contact-line">
      <span>+55 11 98347.2516</span>
      <span class="contact-dot"></span>
      <span>lucinda@velarien-example.com</span>
      <span class="contact-dot"></span>
      <span>velarien-example.com</span>
    </p>
  </section>

  <section class="card card--back" aria-label="Business card back">
    <p class="back-brand">VELARIEN</p>
  </section>
</body>
</html>
```